Harborline Pension Group Needs a Fresh Business Card Update!

We are looking forward to a busy year ahead and have just launched our new website. We are looking to you for a fresh update to our business cards!

Here is a link to our website: http://www.harborlinepensiongrp.com/

You will find our logo attached in two formats for your use. Our old business card front and back is also attached for your reference. We want to have a portrait space on the new cards similar to the old card that we can interchange with various employee portraits or keep blank.
We are also interested in seeing a play on colors that matches our website and logo.

For the back of the card please make the following changes (from our old card):

1. The new "FREE REPORT" is titled as follows: FREE REPORT - Six Pitfalls That Drain Nest Eggs

2. Under "How Can We Help You?" please list out the following in place of the longer list:

Determine Retirement Eligibility & Best Date for You to Retire
Organizing Important Documents for Retirement
Calculate your annuity estimate
Completing Retirement Paperwork
Survivor Benefit Options
Deposits and Re-deposits
Military Service
Social Security Questions
CAPD Special Supplement
Health Insurance
Early-Out Options
Meadow Reserve Fund (during service and after retirement)

3. Under: "Am I on Track to Retire?" please edit the sentence to read:
Find out by Scheduling a "FREE" Federal Benefit & Analysis Counseling Session

Designers, Thank you for your creativity!

Target Market(s)

Federal Employees ages 45-65

Industry/Entity Type

Financial Planning

Contact Information for Business Card

We want to have a portrait space on the front of the new cards similar to the old card that we can interchange with various employee portraits or keep blank. The only text that is negotiable on the front of the card is the bulleted text.
We would like for you to use colors that match our website and logo.

Survivor Benefit Options
Deposits and Re-deposits
Military Service
Social Security Questions
CAPD Special Supplement
Health Insurance
Early-Out Options

Font styles to use
Serif

Requirements
Must have
• Colors to match our logo and new website: http://www.harborlinepensiongrp.com/

```html
<!DOCTYPE html>
<html lang="en">
<head>
<meta charset="utf-8">
<title>Harborline Pension Group – Stationery Proof #3</title>
<link href="https://fonts.googleapis.com/css2?family=Arimo&family=Cinzel:wght@600&family=Montserrat:wght@400;500;600;700&display=swap" rel="stylesheet">
<style>
:root{
  --board:#e4e1dd;
  --label:#7d7d7d;
  --navy:#16202f;
  --red:#d42027;
  --blue:#2a7bc4;
  --sky:#7fb0d6;
  --mist:#ececec;
  --ink:#222222;
  --paper:#ffffff;
}
*{box-sizing:border-box;margin:0;padding:0}
html,body{width:1200px;height:1200px;overflow:hidden}
body{background:var(--board);position:relative;font-family:"Montserrat",sans-serif;color:var(--ink)}
.label{position:absolute;font-family:"Arimo",sans-serif;color:var(--label);font-size:35px;line-height:1;letter-spacing:.5px}
.piece{position:absolute;background:var(--paper);box-shadow:0 2px 8px rgba(0,0,0,.22);overflow:hidden}
.brand{display:flex;flex-direction:column;align-items:center;text-align:center}
.brand-mark{border-radius:50%;border:2px solid var(--navy);background:var(--paper)}
.brand-name{font-family:"Cinzel",serif;font-weight:600;color:var(--blue);line-height:1.1}
.contact{font-size:6.4px;text-align:center;line-height:1.3;font-weight:500;color:var(--ink)}
.gap{margin-top:5px}

/* business card front */
.card-front{left:642px;top:51px;width:230px;height:406px}
.card-front .top{height:163px;background:var(--navy);padding-top:34px}
.card-front .brand-mark{width:58px;height:58px;border-color:var(--paper);background:var(--navy)}
.card-front .brand-name{font-size:19px;margin-top:16px;width:200px}
.card-front .motto{height:50px;background:var(--red);color:var(--paper);font-size:8.4px;font-weight:700;letter-spacing:2.6px;padding:8px 0 0 14px;line-height:1.45;white-space:nowrap}
.card-front .person{height:97px;background:var(--mist);text-align:center;padding-top:11px}
.card-front .focus{font-size:9.4px;line-height:1.25}
.card-front .name{color:var(--red);font-weight:700;font-size:14px;margin-top:7px}
.card-front .email{font-weight:600;font-size:10.4px;margin-top:5px}
.card-front .details{height:96px;background:var(--sky);text-align:center;font-size:9.2px;font-weight:600;line-height:1.25;padding-top:9px}

/* business card back */
.card-back{left:902px;top:51px;width:231px;height:406px}
.card-back .top{height:107px;background:var(--navy);position:relative}
.card-back .brand{position:absolute;left:12px;top:44px;width:120px}
.card-back .brand-mark{width:28px;height:28px;border-color:var(--paper);background:var(--navy)}
.card-back .brand-name{font-size:10.5px;margin-top:5px}
.portrait{position:absolute;left:136px;top:15px;width:80px;height:80px;border-radius:50%;border:2px solid var(--paper);background:radial-gradient(circle at 50% 40%,#b9b9b9,#5c5c5c)}
.card-back .services{background:var(--mist);height:248px;text-align:center;padding-top:10px}
.heading{color:var(--red);font-weight:700;font-size:10.6px;letter-spacing:2.4px}
.service-list{list-style:none;font-size:8.7px;font-weight:600;line-height:1.28;margin-top:4px}
.card-back .cta{font-size:8.7px;font-weight:600;line-height:1.28;margin-top:2px}
.card-back .heading.second{margin-top:8px}
.free-report{font-size:7.2px;font-weight:600;margin-top:5px;white-space:nowrap}
.free-report strong{color:var(--red);font-weight:700}
.card-back .details{height:51px;background:var(--sky);color:var(--paper);text-align:center;font-size:9.2px;font-weight:600;line-height:1.3;padding-top:12px}

/* letterhead */
.letterhead{left:54px;top:491px;width:514px;height:665px;background:var(--mist)}
.letterhead .header{height:71px;background:var(--paper);position:relative}
.letterhead .brand{position:absolute;left:30px;top:13px;width:118px}
.sheet-mark{width:30px;height:30px}
.sheet-name{font-size:10.5px;margin-top:6px}
.letterhead .contact{position:absolute;left:324px;top:18px;width:164px}
.faint-ring{position:absolute;left:58px;top:113px;width:414px;height:414px;border-radius:50%;border:9px solid #f2f2f2}
.letterhead .foot{position:absolute;left:0;bottom:0;width:100%;height:22px;background:var(--sky)}

/* compliments slip */
.slip{left:630px;top:557px;width:514px;height:221px}
.slip .brand{position:absolute;left:28px;top:13px;width:118px}
.slip .contact{position:absolute;left:326px;top:16px;width:160px}
.slip .rule{position:absolute;left:0;top:78px;width:100%;height:1px;background:var(--blue)}
.slip .rule-text{position:absolute;left:180px;top:72px;background:var(--paper);padding:0 8px;color:var(--blue);font-size:9.6px;font-weight:700;letter-spacing:3.2px}

/* envelope */
.envelope{left:630px;top:882px;width:514px;height:256px}
.envelope .brand{position:absolute;left:16px;top:19px;width:120px}
.envelope .contact{font-size:6.2px;font-weight:400;margin-top:3px;line-height:1.25}
</style>
</head>
<body>

<div class="label" style="left:55px;top:60px">PROOF #3</div>
<div class="label" style="left:324px;top:60px">BUSINESS CARD</div>
<div class="label" style="left:68px;top:418px">LETTERHEAD</div>
<div class="label" style="left:631px;top:501px">WITH COMPLIMENTS SLIP</div>
<div class="label" style="left:631px;top:832px">ENVELOPE</div>

<section class="piece card-front">
  <div class="top brand">
    <div class="brand-mark"></div>
    <div class="brand-name">Harborline Pension Group</div>
  </div>
  <div class="motto">
    <p>INFORMATION YOU NEED</p>
    <p>ADVICE YOU CAN TRUST</p>
    <p>SUPPORT YOU CAN COUNT ON</p>
  </div>
  <div class="person">
    <p class="focus">Dedicated to and Specializing<br>in CRPS/CAPD &amp; the Financial Needs<br>of Federal Employees</p>
    <p class="name">DANA WHITCOMBE</p>
    <p class="email">Dana@DanaWhitcombe.com</p>
  </div>
  <div class="details">
    <p>303-555-0148</p>
    <p>Toll Free: 1-877-555-0192</p>
    <p>Fax 1-888-555-0167</p>
    <p class="gap">410 Cedar Ridge Ave., Suite 210</p>
    <p>Arvada, CO 80002</p>
    <p>www.harborlinepensiongrp.com</p>
  </div>
</section>

<section class="piece card-back">
  <div class="top">
    <div class="brand">
      <div class="brand-mark"></div>
      <div class="brand-name">Harborline Pension Group</div>
    </div>
    <div class="portrait" role="img" aria-label="Employee portrait"></div>
  </div>
  <div class="services">
    <p class="heading">HOW CAN WE HELP YOU?</p>
    <ul class="service-list">
      <li>Determine Retirement Eligibility &amp;<br>Best Date for You to Retire</li>
      <li>Organizing Important Documents<br>for Retirement</li>
      <li>Calculate your annuity estimate</li>
      <li>Completing Retirement Paperwork</li>
      <li>Survivor Benefit Options</li>
      <li>Deposits and Re-deposits</li>
      <li>Military Service</li>
      <li>Social Security Questions</li>
      <li>CAPD Special Supplement</li>
      <li>Health Insurance</li>
      <li>Early-Out Options</li>
      <li>Meadow Reserve Fund</li>
      <li>(during service and after retirement)</li>
    </ul>
    <p class="heading second">AM I ON TRACK TO RETIRE?</p>
    <p class="cta">Find out by Scheduling a “FREE” Federal<br>Benefit &amp; Analysis Counseling Session</p>
    <p class="free-report"><strong>FREE REPORT</strong> – Six Pitfalls That Drain Nest Eggs</p>
  </div>
  <div class="details">
    <p>TOLL FREE: 1-877-555-0192</p>
    <p>www.harborlinepensiongrp.com</p>
  </div>
</section>

<section class="piece letterhead">
  <div class="header">
    <div class="brand">
      <div class="brand-mark sheet-mark"></div>
      <div class="brand-name sheet-name">Harborline Pension Group</div>
    </div>
    <div class="contact">
      <p>303-555-0148</p>
      <p>Toll Free: 1-877-555-0192</p>
      <p>Fax 1-888-555-0167</p>
      <p class="gap">410 Cedar Ridge Ave., Suite 210 Arvada, CO 80002</p>
      <p>www.harborlinepensiongrp.com</p>
    </div>
  </div>
  <div class="faint-ring"></div>
  <div class="foot"></div>
</section>

<section class="piece slip">
  <div class="brand">
    <div class="brand-mark sheet-mark"></div>
    <div class="brand-name sheet-name">Harborline Pension Group</div>
  </div>
  <div class="contact">
    <p>303-555-0148</p>
    <p>Toll Free: 1-877-555-0192</p>
    <p>Fax 1-888-555-0167</p>
    <p class="gap">410 Cedar Ridge Ave., Suite 210 Arvada, CO 80002</p>
    <p>www.harborlinepensiongrp.com</p>
  </div>
  <div class="rule"></div>
  <div class="rule-text">WITH COMPLIMENTS</div>
</section>

<section class="piece envelope">
  <div class="brand">
    <div class="brand-mark sheet-mark"></div>
    <div class="brand-name sheet-name">Harborline Pension Group</div>
    <div class="contact">
      <p>303-555-0148</p>
      <p>Toll Free: 1-877-555-0192</p>
      <p>Fax 1-888-555-0167</p>
      <p>410 Cedar Ridge Ave., Suite 210</p>
      <p>Arvada, CO 80002</p>
      <p>www.harborlinepensiongrp.com</p>
    </div>
  </div>
</section>

</body>
</html>
```